Plindy Orchards Business Card Design

My company is about Natural products made from Bees Wax, of which I am farming/raising. Products like Honey when in season, body butter, hand cream, lotions, lip balm, soap and more! All Natural, with Beeswax as the base, as it has large healing properties for moisturizing and nourishing your skin.
I would prefer lots of yellows, browns, and blacks (but am open)! I think black ink on the artwork may show up the best. But your the professionals!
The artwork is very dear to me, as my son, Warren did this in the hospital when he was diagnosed with Leukemia, of which he did not survive, at eighteen.
Is it possible to put his initials on this? WDT in light colored ink.
NO BEES, NO US! Oops! I need my name on there. Paula Vantreck and number 210-555-0147. Thank you all so much.

Hospital

Plindy Orchards
All Natural Products
Paula Vantreck
210-555-0147
PlindyOrchards@mailbrook.example

```html
<!DOCTYPE html>
<html lang="en">
<head>
<meta charset="utf-8">
<title>Plindy Orchards Business Card</title>
<link rel="stylesheet" href="https://fonts.googleapis.com/css2?family=Quicksand:wght@300;400;500;700&display=swap">
<style>
  :root {
    --stage: #e9e8e5;
    --card-yellow: #ecd43a;
    --brown: #6b4a2b;
    --panel-white: #ffffff;
    --contact-orange: #ea9a45;
    --initials-light: #fdf6e0;
    --art-red: #e0304a;
    --art-orange: #f08a2a;
    --art-yellow: #f5d23a;
    --art-blue: #2f7fc4;
    --art-green: #6cbf4a;
    --art-pink: #e85a9a;
    --art-purple: #7a3f9e;
  }
  * { box-sizing: border-box; margin: 0; padding: 0; }
  html, body {
    width: 1200px;
    height: 899px;
    overflow: hidden;
    background: var(--stage);
  }
  .business-card {
    position: absolute;
    left: 100px;
    top: 164px;
    width: 1000px;
    height: 571px;
    background: var(--card-yellow);
    font-family: "Quicksand", sans-serif;
    box-shadow: 0 6px 18px rgba(0,0,0,0.18);
    overflow: hidden;
  }
  .brand-title {
    position: absolute;
    left: 44px;
    top: 26px;
    font-size: 72px;
    font-weight: 700;
    letter-spacing: 4px;
    color: var(--brown);
    text-transform: uppercase;
    white-space: nowrap;
    line-height: 1.2;
  }
  .artwork {
    position: absolute;
    left: 0;
    top: 140px;
    width: 560px;
    height: 305px;
    background:
      radial-gradient(circle at 22% 70%, var(--art-red) 0 18%, transparent 34%),
      radial-gradient(circle at 75% 30%, var(--art-green) 0 10%, transparent 28%),
      radial-gradient(circle at 85% 75%, var(--art-blue) 0 14%, transparent 32%),
      radial-gradient(circle at 50% 15%, var(--art-orange) 0 12%, transparent 30%),
      radial-gradient(circle at 10% 25%, var(--art-purple) 0 10%, transparent 28%),
      radial-gradient(circle at 55% 85%, var(--art-pink) 0 12%, transparent 30%),
      linear-gradient(135deg, var(--art-yellow), var(--art-orange) 40%, var(--art-red) 70%, var(--art-blue));
  }
  .artist-initials {
    position: absolute;
    right: 16px;
    bottom: 10px;
    font-size: 18px;
    font-weight: 500;
    letter-spacing: 2px;
    color: var(--initials-light);
  }
  .contact-panel {
    position: absolute;
    left: 560px;
    top: 140px;
    width: 440px;
    height: 305px;
    background: var(--panel-white);
    padding: 48px 0 0 34px;
    color: var(--contact-orange);
    font-weight: 300;
  }
  .contact-name { font-size: 38px; line-height: 1.15; }
  .contact-phone { font-size: 44px; line-height: 1.15; letter-spacing: 1px; }
  .contact-email { font-size: 21px; line-height: 1.5; font-weight: 400; }
  .tagline {
    position: absolute;
    left: 0;
    top: 445px;
    width: 1000px;
    height: 126px;
    line-height: 126px;
    text-align: center;
    font-size: 28px;
    font-weight: 400;
    color: var(--brown);
    letter-spacing: 0.5px;
  }
</style>
</head>
<body>
  <div class="business-card">
    <h1 class="brand-title">Plindy Orchards</h1>
    <div class="artwork" role="img" aria-label="Colourful hand-painted abstract artwork with swirls of red, orange, yellow, green, blue and pink">
      <span class="artist-initials">WDT</span>
    </div>
    <div class="contact-panel">
      <p class="contact-name">Paula Vantreck</p>
      <p class="contact-phone">210-555-0147</p>
      <p class="contact-email">PlindyOrchards@mailbrook.example</p>
    </div>
    <p class="tagline">plindy orchards - all natural products</p>
  </div>
</body>
</html>
```